Redesign of Real Estate Agency Website

We need a redesign for our real estate agency website. Please see attached creative brief.

Target Market(s)

Refer to creative brief.

Industry/Entity Type

Real Estate

Requirements
Must have
• Refer to creative brief.

```html
<!DOCTYPE html>
<html lang="en">
<head>
<meta charset="utf-8">
<title>Andaman Nest – Canopy Residence</title>
<link href="https://fonts.googleapis.com/css2?family=Mulish:wght@300;400;700&family=Roboto+Condensed:wght@400;700&family=Libre+Baskerville&display=swap" rel="stylesheet">
<style>
:root{
  --blue:#2a9fdb;
  --blue-dark:#1677b3;
  --sky:#e4f3fc;
  --ink:#222;
  --muted:#444;
  --line:#cfd6dc;
  --panel:#f4f4f4;
  --red:#e2262b;
}
*{box-sizing:border-box;margin:0;padding:0}
html,body{width:980px;height:1200px;overflow:hidden;background:#fff}
body{font-family:"Mulish",sans-serif;color:var(--ink)}
.page{position:relative;width:1200px;height:1470px;transform:scale(.816667);transform-origin:0 0}
.abs{position:absolute}
.header{left:123px;top:0;width:960px;height:121px;background:var(--sky);border-bottom:1px solid var(--line)}
.brand{left:171px;top:26px;font-family:"Libre Baskerville",serif;font-size:24px;color:#333}
.brand-tag{left:172px;top:53px;font-size:9px;color:#555;letter-spacing:.3px}
.office{left:650px;top:36px;display:flex;align-items:center;gap:8px;font-size:16px;color:#222}
.btn-top{top:34px;height:26px;border-radius:4px;background:linear-gradient(#4fb6ea,var(--blue-dark));color:#fff;font-size:11px;font-family:"Libre Baskerville",serif;display:flex;align-items:center;justify-content:center}
.nav{left:123px;top:90px;width:960px;display:flex;align-items:center;font-size:15px;color:#222}
.nav span{position:absolute;top:2px;white-space:nowrap}
.nav .active{background:#333;color:#fff;border-radius:10px;padding:1px 14px;top:1px}
.panel{background:linear-gradient(#fff,var(--panel));border:1px solid #ddd;box-shadow:0 1px 3px rgba(0,0,0,.2)}
.band{background:linear-gradient(#5cc0f0,var(--blue));color:#fff;font-size:23px;font-weight:300;padding:8px 24px}
.radio{font-size:12px;display:flex;align-items:center;gap:8px;font-family:"Libre Baskerville",serif}
.radio.on{background:var(--blue);color:#fff;border-radius:4px;padding:3px 10px}
.dot{width:10px;height:10px;border-radius:50%;background:#fff;border:2px solid #fff;box-shadow:inset 0 0 0 2px var(--blue)}
.radio:not(.on) .dot{background:#ddd;box-shadow:none;border-color:#ddd}
.select{height:26px;border:1px solid #ccc;background:#fff;font-size:9px;color:#444;padding:7px 9px;box-shadow:inset 0 1px 2px rgba(0,0,0,.06)}
.select::after{content:"";position:absolute;right:3px;top:4px;width:15px;height:16px;background:#e8e8e8;border:1px solid #bbb;border-radius:2px}
.select i{position:absolute;right:7px;top:10px;border:4px solid transparent;border-top:5px solid #555;z-index:1}
.map{background:linear-gradient(160deg,#2a8fc9,#5cb5e0 60%,#3d9fd4);border:3px solid #fff;box-shadow:0 0 3px rgba(0,0,0,.3)}
.small{font-size:9px;color:#333;line-height:19px}
.btn{background:linear-gradient(#4fb9ec,var(--blue-dark));color:#fff;font-weight:700;font-size:10px;border-radius:4px;display:flex;align-items:center;justify-content:center;letter-spacing:.5px}
.h-blue{font-size:23px;color:var(--blue);font-weight:300;white-space:nowrap}
.list{list-style:none;font-size:9px;line-height:17px}
.list li::before{content:"•";display:inline-block;width:20px;color:#111}
.list li.hi{color:var(--blue);font-weight:700}
.list li.hi::before{color:var(--blue)}
.field{height:22px;border:1px solid #aaa;background:#fff}
.photo{background:linear-gradient(#516244,#2f3c26 55%,#4d5048)}
.caption{background:rgba(255,255,255,.75);font-family:"Roboto Condensed",sans-serif;font-size:24px;color:var(--blue);padding:0 12px;line-height:32px;height:32px;white-space:nowrap}
.caption b{color:#333}
.title-band{background:linear-gradient(#65c4f2,var(--blue));color:#fff;font-family:"Libre Baskerville",serif;font-size:19px;text-align:center;line-height:34px;border-bottom:2px solid #1d7fb9}
.spec{font-size:12px;position:absolute;white-space:nowrap}
.spec b{font-weight:700}
.lbl{font-size:11px;color:#333}
.footer{left:123px;top:1357px;width:960px;height:113px;background:var(--sky);border-top:3px solid var(--blue)}
.fh{font-size:16px;color:var(--blue-dark);font-weight:300}
.flist{list-style:none;font-size:9px;line-height:23.5px;color:#333}
.flist li::before{content:"";display:inline-block;border:4px solid transparent;border-left:5px solid #777;margin-right:8px}
.social{width:25px;height:25px;border-radius:4px}
</style>
</head>
<body>
<div class="page">

<header class="abs header"></header>
<div class="abs brand">Andaman Nest</div>
<div class="abs brand-tag">ANDAMAN PROPERTY &amp; REAL ESTATE</div>
<div class="abs office">
  <svg width="28" height="24" viewBox="0 0 28 24"><path d="M4 20 L20 4 L24 8 L8 22 Z" fill="#333"/><path d="M2 22 Q6 16 10 20" stroke="#333" fill="none" stroke-width="1.5"/></svg>
  <span>OFFICE &nbsp; +48 20 55 66 777</span>
</div>
<div class="abs btn-top" style="left:907px;width:64px">LOGIN</div>
<div class="abs btn-top" style="left:977px;width:64px">SIGN UP</div>

<nav class="abs nav">
  <span style="left:16px">Home</span>
  <span style="left:115px">Property for Rent</span>
  <span style="left:275px">Property for Sale</span>
  <span class="active" style="left:408px">About Us</span>
  <span style="left:516px">Contact Us</span>
  <span style="left:630px">List your Property</span>
  <span style="left:785px">Property Buyer’s Guide</span>
</nav>

<section class="abs panel" style="left:133px;top:127px;width:276px;height:618px"></section>
<div class="abs band" style="left:141px;top:132px;width:261px;height:43px">Search a Property:</div>
<div class="abs radio on" style="left:157px;top:187px"><span class="dot"></span>To Buy</div>
<div class="abs radio" style="left:258px;top:190px"><span class="dot"></span>To Rent</div>
<div class="abs select" style="left:155px;top:221px;width:214px">Property Type:<i></i></div>
<div class="abs select" style="left:155px;top:254px;width:214px">Search Area:<i></i></div>
<div class="abs select" style="left:155px;top:288px;width:99px">Price Range:<i></i></div>
<div class="abs select" style="left:270px;top:288px;width:99px">To:<i></i></div>
<div class="abs select" style="left:155px;top:321px;width:99px">Bedroom(s):<i></i></div>
<div class="abs select" style="left:270px;top:321px;width:99px">Bathroom(s):<i></i></div>
<div class="abs band" style="left:141px;top:364px;width:261px;height:43px">Search by map:</div>
<div class="abs map" role="img" aria-label="Island map with clickable areas" style="left:197px;top:422px;width:148px;height:245px"></div>
<p class="abs small" style="left:146px;top:680px">Know exactly what you want? Try our</p>
<p class="abs small" style="left:147px;top:698px;color:var(--red);text-decoration:underline">Advanced search</p>
<div class="abs btn" style="left:291px;top:705px;width:98px;height:26px">Start Searching</div>

<section class="abs panel" style="left:133px;top:758px;width:276px;height:152px"></section>
<h2 class="abs h-blue" style="left:149px;top:763px;font-size:21px">Browse Property for Sale</h2>
<ul class="abs list" style="left:153px;top:795px">
  <li>Hot Properties &amp; Promotions</li>
  <li>Apartments &amp; Condos</li>
  <li>Villas &amp; Houses</li>
  <li>Land</li>
  <li class="hi">Commercial</li>
  <li>Property Buyer’s Guide</li>
</ul>

<section class="abs panel" style="left:133px;top:923px;width:276px;height:152px"></section>
<h2 class="abs h-blue" style="left:149px;top:927px">Newsletter</h2>
<p class="abs small" style="left:149px;top:955px">Etiam tincidunt cursus nibh, nec porttitor est...</p>
<span class="abs small" style="left:150px;top:986px">Your name:</span>
<div class="abs field" style="left:217px;top:984px;width:158px"></div>
<span class="abs small" style="left:150px;top:1019px">Your e-mail:</span>
<div class="abs field" style="left:217px;top:1019px;width:158px"></div>
<div class="abs btn" style="left:291px;top:1045px;width:98px;height:26px">Subscribe</div>

<section class="abs panel" style="left:413px;top:127px;width:666px;height:259px"></section>
<div class="abs photo" role="img" aria-label="Terrace view over a green forested hillside" style="left:417px;top:131px;width:553px;height:251px"></div>
<div class="abs caption" style="right:240px;top:344px">CANOPY RESIDENCE - <b>KAMALA</b></div>
<div class="abs" role="img" aria-label="Bright living room interior" style="left:975px;top:131px;width:100px;height:62px;background:linear-gradient(#e8eef0,#c9d2cf)"></div>
<div class="abs" role="img" aria-label="Bedroom with white linen" style="left:975px;top:208px;width:100px;height:63px;background:linear-gradient(#e9e2d2,#cdb98e)"></div>
<div class="abs" role="img" aria-label="Building among trees with pool" style="left:975px;top:287px;width:100px;height:62px;background:linear-gradient(#c7dbe0,#5f8b4b)"></div>
<div class="abs btn" style="left:975px;top:359px;width:100px;height:22px;border-radius:0;font-size:9px">MORE IMAGES</div>

<section class="abs panel" style="left:413px;top:393px;width:666px;height:949px"></section>
<div class="abs title-band" style="left:425px;top:397px;width:641px;height:34px">CANOPY RESIDENCE</div>

<span class="spec" style="left:427px;top:452px"><b>Bedrooms:</b></span><span class="spec" style="left:529px;top:452px">4</span>
<span class="spec" style="left:427px;top:477px"><b>Bathrooms:</b></span><span class="spec" style="left:529px;top:477px">3</span>
<span class="spec" style="left:427px;top:503px"><b>Price:</b></span><span class="spec" style="left:529px;top:503px;color:var(--blue)">THB 7.6M</span>
<span class="spec" style="left:427px;top:528px"><b>View:</b></span><span class="spec" style="left:529px;top:528px">Sea View</span>
<span class="spec" style="left:427px;top:553px"><b>Type:</b></span><span class="spec" style="left:529px;top:553px">Apartment/Condo</span>
<span class="spec" style="left:715px;top:452px"><b>Living Area:</b></span><span class="spec" style="left:817px;top:452px">157 sqm</span>
<span class="spec" style="left:715px;top:477px"><b>Swimming Pool:</b></span><span class="spec" style="left:817px;top:477px">Shared</span>
<span class="spec" style="left:715px;top:503px"><b>Car Parking:</b></span><span class="spec" style="left:817px;top:503px">Shared</span>
<span class="spec" style="left:715px;top:528px"><b>Furnished:</b></span><span class="spec" style="left:817px;top:528px">Fully-furnished</span>
<span class="spec" style="left:715px;top:553px"><b>Reference no.:</b></span><span class="spec" style="left:817px;top:553px">1591</span>
<div class="abs map" role="img" aria-label="Island map marking Kamala location" style="left:919px;top:437px;width:147px;height:244px"></div>

<p class="abs small" style="left:427px;top:591px;width:470px"><b>2-bedroom apartments offer 157 sqm</b>, featuring quality local materials with natural finishes to create a relaxed and stylish living space.<br><b>Fully furnished and are designed to take advantage of the surrounding environment.</b> Large sliding doors and windows, as well as walk around terraces, help to maximize the stunning views and natural breezes.</p>
<div class="abs" style="left:427px;top:703px;width:634px;border-top:1px dashed #bbb"></div>
<p class="abs small" style="left:427px;top:720px;width:636px">To request more information about this property, please provide us with your email address, name and any questions that you might have. We will respond within 24 hours.</p>
<p class="abs small" style="left:427px;top:777px">We look forward to assisting you.</p>
<p class="abs small" style="left:427px;top:814px;width:636px">To submit an inquiry for multiple properties click "Add to Inquiry Cart". You will be taken the Inquiry Cart page where you can review items and then continue to inquiry form or add more properties.</p>
<div class="abs" style="left:428px;top:864px;width:200px;height:31px;border:1px solid #bbb;border-radius:6px;background:linear-gradient(#fff,#eee);color:var(--blue-dark);font-family:'Roboto Condensed',sans-serif;font-size:16px;font-weight:700;display:flex;align-items:center;justify-content:center">Add to Inquiry Cart</div>
<p class="abs small" style="left:427px;top:905px">Alternatively, to submit an inquiry for this property only, complete the form below and click "<b>Send</b>".</p>
<p class="abs small" style="left:427px;top:937px;font-style:italic"><span style="color:var(--red)">*</span> indicates a required field.</p>

<span class="abs lbl" style="left:435px;top:977px">Your name <span style="color:var(--red)">*</span></span>
<div class="abs field" style="left:519px;top:973px;width:166px"></div>
<span class="abs lbl" style="left:435px;top:1016px">Your email <span style="color:var(--red)">*</span></span>
<div class="abs field" style="left:519px;top:1011px;width:166px"></div>
<span class="abs lbl" style="left:435px;top:1047px;line-height:14px">Country of<br>residence</span>
<div class="abs select" style="left:519px;top:1048px;width:299px;height:24px;padding-top:6px">Please select<i></i></div>
<span class="abs lbl" style="left:435px;top:1091px">Phone number</span>
<div class="abs field" style="left:519px;top:1086px;width:166px"></div>
<span class="abs lbl" style="left:435px;top:1128px">Comments</span>
<div class="abs field" style="left:519px;top:1123px;width:299px;height:128px"></div>
<div class="abs btn" style="left:519px;top:1259px;width:79px;height:20px">Send</div>
<p class="abs" style="left:519px;top:1288px;font-size:12px;color:var(--blue-dark)">Or call us on +66 (0) 800 000 123</p>
<p class="abs small" style="left:427px;top:1309px">We value your privacy and will not share this information with third parties. Please see our <b style="color:var(--blue-dark)">privacy policy</b> for more details.</p>

<footer class="abs footer"></footer>
<h3 class="abs fh" style="left:156px;top:1367px">ABOUT US</h3>
<ul class="abs flist" style="left:156px;top:1388px"><li>Company Info</li><li>Our Services</li><li>Clients</li></ul>
<h3 class="abs fh" style="left:292px;top:1367px">JOIN IN</h3>
<ul class="abs flist" style="left:292px;top:1388px"><li>FAQ`s</li><li>Solutions</li><li>Contacts</li></ul>
<h3 class="abs fh" style="left:419px;top:1367px">ADVICE</h3>
<ul class="abs flist" style="left:419px;top:1388px"><li>Sign Up</li><li>Blog</li><li>Promotions</li></ul>
<div class="abs" style="left:551px;top:1372px;display:flex;gap:6px">
  <span class="social" style="background:#f07a22"></span>
  <span class="social" style="background:#3b5a9a"></span>
  <span class="social" style="background:#3fb2e4"></span>
  <span class="social" style="background:#2b9f5d"></span>
  <span class="social" style="background:#f58d1e"></span>
</div>
<p class="abs" style="left:550px;top:1413px;font-size:14px;color:var(--blue-dark);white-space:nowrap">ANDAMAN NEST PROPERTY <span style="font-size:9px;color:#333">&nbsp;© 2010 &nbsp;| &nbsp;Privacy Policy</span></p>
<p class="abs" style="left:550px;top:1440px;font-size:9px;color:#333;white-space:nowrap"><b style="color:var(--blue-dark)">Home</b> | Property for Rent | Property for Sale | About | Contact us | List your Property | Property Buyer’s Guide</p>

</div>
</body>
</html>
```